Website Design - Photo Shop Design - Functional Cash Register Layout for POS System

Design a webpage for Point of Sale site. A cash register page.

Page must have a good look. I have attached a file of a possible layout example - but need a much nicer design. I have also attached the site logo. which i will upload without background tomorrow hopefully.

Looking for a nice Fresh look , not dark and dingy.

Target Market(s)

Business

Industry/Entity Type

Business Software

Number of Pages Required

1 page

Colors
f59195
f04a50
ec1f27
fbd4d5
ffffff
f8f3f8
fdf0f6
feeeee
ecf5f6

Requirements
Must have
• Cash register layout for POS software site. Nice layout ,
Nice to have
• Try putting he register part on the left side as well as the right - invert the designs have them different to the layout example shown too.
Should not have
• Not to dark

```html
<!DOCTYPE html>
<html lang="en">
<head>
<meta charset="utf-8">
<title>TillNest – Cash Register</title>
<link href="https://fonts.googleapis.com/css2?family=Questrial&display=swap" rel="stylesheet">
<style>
:root{
  --red:#ec1f27;
  --red-soft:#f04a50;
  --red-bar:rgba(236,31,39,.94);
  --white:#ffffff;
  --ink:#1e1e1e;
  --grey-text:#6d6d6d;
  --grey-line:#d9d9d9;
  --stage:#efefef;
  --photo:linear-gradient(180deg,#b7a58a 0%,#8c9a6a 35%,#6b4a33 60%,#4b3324 100%);
}
*{box-sizing:border-box;margin:0;padding:0}
html,body{width:1200px;height:678px;overflow:hidden}
body{position:relative;background:var(--white);font-family:"Questrial",sans-serif;color:var(--ink)}

/* register column */
.register{position:absolute;left:0;top:0;width:381px;height:678px;background:var(--white);overflow:hidden;border-right:1px solid #e6e6e6}
.register-head{position:absolute;left:0;top:0;width:381px;height:131px;background:var(--red);color:var(--white)}
.cashier{position:absolute;left:28px;top:31px;width:322px;height:32px;border-bottom:1px solid rgba(255,255,255,.7);display:flex;align-items:flex-start}
.cashier svg{width:22px;height:22px;margin-right:15px}
.cashier-name{font-size:17px;line-height:22px}
.cashier-name b{font-weight:700}
.cashier-time{margin-left:auto;font-size:17px;line-height:22px}
.transaction{position:absolute;left:28px;top:86px;width:322px;display:flex;align-items:center}
.transaction-label{font-size:17px}
.transaction-label b{font-weight:700}
.transaction-tools{margin-left:auto;display:flex;gap:18px}
.transaction-tools svg{width:24px;height:24px}

.group-title{position:absolute;left:28px;width:322px;padding-bottom:8px;border-bottom:1px solid var(--grey-line);color:var(--red);font-size:16px;font-weight:700}
.line-item{position:absolute;left:28px;width:322px;height:66px}
.thumb{position:absolute;left:0;top:0;width:66px;height:66px;border-radius:50%;background:var(--photo)}
.thumb.removing::after{content:"";position:absolute;inset:0;border-radius:50%;background:rgba(236,31,39,.88)}
.thumb.removing svg{position:absolute;left:23px;top:23px;width:20px;height:20px;z-index:1}
.item-name{position:absolute;left:78px;top:17px;color:var(--red);font-size:17.5px}
.item-size{position:absolute;left:78px;top:38px;color:var(--grey-text);font-size:10.5px}
.item-price{position:absolute;right:3px;top:17px;font-size:17.5px}
.item-was{position:absolute;right:3px;top:40px;font-size:10.5px;color:var(--grey-text);text-decoration:line-through}

.payment{position:absolute;left:0;top:608px;width:381px;height:70px;background:var(--red-bar);color:var(--white);display:flex;align-items:center;padding:0 28px 0 27px;font-size:17.5px}
.payment svg{width:14px;height:14px;margin-left:11px}
.payment-total{margin-left:auto}

/* catalogue */
.topbar{position:absolute;left:381px;top:0;width:819px;height:130px;background:var(--white)}
.tab{position:absolute;top:41px;height:45px;line-height:45px;font-size:17.5px;color:var(--grey-text)}
.tab.active{left:42px;width:82px;text-align:center;border:2px solid var(--red);color:var(--red)}
.tab.clothes{left:157px}
.tab.underwear{left:265px}
.topbar .search{position:absolute;left:397px;top:48px;width:28px;height:28px}
.brand{position:absolute;left:475px;top:38px;display:flex;align-items:center;gap:10px;color:var(--ink);font-size:40px;line-height:46px}
.brand-dot{width:26px;height:26px;border-radius:50%;background:var(--red)}

.catalogue{position:absolute;left:381px;top:130px;width:819px;height:548px;background:var(--stage);overflow:hidden}
.product{position:absolute;width:198px;height:198px;border-radius:8px;background:var(--white);overflow:hidden}
.product-photo{height:153px;background:var(--photo)}
.product-name{height:45px;line-height:45px;text-align:center;font-size:17px;white-space:nowrap}
.product.selected{padding:12px}
.selected-frame{height:174px;border:2px solid var(--red);border-radius:7px;text-align:center}
.selected-frame .product-name{height:auto;line-height:1;color:var(--red);margin-top:78px}
.selected-price{font-size:17px;margin-top:21px}
.selected-stock{font-size:11px;color:var(--grey-text);margin-top:24px}
</style>
</head>
<body>

<aside class="register">
  <header class="register-head">
    <div class="cashier">
      <svg viewBox="0 0 24 24" fill="none" stroke="#fff" stroke-width="2"><circle cx="10" cy="10" r="8"/><circle cx="10" cy="8" r="3"/><path d="M5 15c1.5-2.5 8.5-2.5 10 0"/><path d="M16 16l6 6"/></svg>
      <span class="cashier-name"><b>Jonas</b> Weller</span>
      <span class="cashier-time">11:15 am</span>
    </div>
    <div class="transaction">
      <span class="transaction-label">Transaction #<b>1535</b></span>
      <div class="transaction-tools">
        <svg viewBox="0 0 24 24" fill="none" stroke="#fff" stroke-width="1.8"><path d="M2 13l6 8L22 3"/><path d="M6 12l2 4"/></svg>
        <svg viewBox="0 0 24 24" fill="none" stroke="#fff"><circle cx="12" cy="12" r="8" stroke-width="4" stroke-dasharray="3.2 3.08"/><circle cx="12" cy="12" r="6" stroke-width="2.2"/></svg>
        <svg viewBox="0 0 24 24" fill="none" stroke="#fff" stroke-width="1.8"><path d="M4 20l2-6L18 2l4 4L10 18z"/><path d="M15 5l4 4"/></svg>
      </div>
    </div>
  </header>

  <h2 class="group-title" style="top:161px">Boots</h2>

  <div class="line-item" style="top:217px">
    <div class="thumb" role="img" aria-label="Brown leather lace-up boots"></div>
    <span class="item-name">New boots No. 1</span>
    <span class="item-size">Size: 46</span>
    <span class="item-price">$55.30</span>
    <span class="item-was">$89.99</span>
  </div>

  <div class="line-item" style="top:317px">
    <div class="thumb removing" role="img" aria-label="Brown leather lace-up boots marked for removal">
      <svg viewBox="0 0 20 20" stroke="#fff" stroke-width="2"><path d="M2 2l16 16M18 2L2 18"/></svg>
    </div>
    <span class="item-name">New boots No. 1</span>
    <span class="item-size">Size: 46</span>
    <span class="item-price">$55.30</span>
  </div>

  <h2 class="group-title" style="top:420px">Clothes</h2>

  <div class="line-item" style="top:476px">
    <div class="thumb" role="img" aria-label="Brown leather lace-up boots"></div>
    <span class="item-name">New boots No. 1</span>
    <span class="item-size">Size: 46</span>
    <span class="item-price">$55.30</span>
  </div>

  <div class="line-item" style="top:575px">
    <div class="thumb" role="img" aria-label="Brown leather lace-up boots"></div>
    <span class="item-name">New boots No. 1</span>
    <span class="item-size">Size: 46</span>
    <span class="item-price">$55.30</span>
  </div>

  <div class="payment">
    <span>Payment</span>
    <svg viewBox="0 0 14 14" fill="none" stroke="#fff" stroke-width="1.5"><path d="M2 1l10 6-10 6z"/></svg>
    <span class="payment-total">$221.20</span>
  </div>
</aside>

<nav class="topbar">
  <span class="tab active">Boots</span>
  <span class="tab clothes">Clothes</span>
  <span class="tab underwear">Underwear</span>
  <svg class="search" viewBox="0 0 28 28" fill="none" stroke="#555" stroke-width="2"><circle cx="11" cy="11" r="8.5"/><path d="M17.5 17.5l8 8" stroke-width="3"/></svg>
  <div class="brand"><span class="brand-dot"></span><span>TillNest</span></div>
</nav>

<main class="catalogue">
  <div class="product" style="left:18px;top:20px"><div class="product-photo" role="img" aria-label="Brown leather lace-up boots"></div><div class="product-name">New boots No. 1</div></div>
  <div class="product" style="left:233px;top:20px"><div class="product-photo" role="img" aria-label="Brown leather lace-up boots"></div><div class="product-name">New boots No. 1</div></div>
  <div class="product" style="left:449px;top:20px"><div class="product-photo" role="img" aria-label="Brown leather lace-up boots"></div><div class="product-name">New boots No. 1</div></div>
  <div class="product" style="left:666px;top:20px"><div class="product-photo" role="img" aria-label="Brown leather lace-up boots"></div><div class="product-name">New boots No. 1</div></div>

  <div class="product" style="left:18px;top:236px"><div class="product-photo" role="img" aria-label="Brown leather lace-up boots"></div><div class="product-name">New boots No. 1</div></div>
  <div class="product selected" style="left:233px;top:236px">
    <div class="selected-frame">
      <div class="product-name">New boots No. 1</div>
      <div class="selected-price">$55.30</div>
      <div class="selected-stock">853 in warehouse</div>
    </div>
  </div>
  <div class="product" style="left:449px;top:236px"><div class="product-photo" role="img" aria-label="Brown leather lace-up boots"></div><div class="product-name">New boots No. 1</div></div>
  <div class="product" style="left:666px;top:236px"><div class="product-photo" role="img" aria-label="Brown leather lace-up boots"></div><div class="product-name">New boots No. 1</div></div>

  <div class="product" style="left:18px;top:454px"><div class="product-photo" role="img" aria-label="Brown leather lace-up boots"></div></div>
  <div class="product" style="left:233px;top:454px"><div class="product-photo" role="img" aria-label="Brown leather lace-up boots"></div></div>
  <div class="product" style="left:449px;top:454px"><div class="product-photo" role="img" aria-label="Brown leather lace-up boots"></div></div>
  <div class="product" style="left:666px;top:454px"><div class="product-photo" role="img" aria-label="Brown leather lace-up boots"></div></div>
</main>

</body>
</html>
```